Bus Card for Organic Hydroponic Produce company

We need a business card for a budding new business. We grow 100% organic, 100% hydroponic, 100% GMO free produce for sale in our local area. We need something bold and dynamic, not simple and elegant. We want to catch peoples attention and get them to visit our website to view more information about our products and services. Its difficult to explain on a business card the differences between our produce (tomatoes, cucumbers, peppers, etc...) and the kind they would buy at the local grocer or market. , so we need to push them to the website.
We have been brainstorming names for the company and have a few in mind, so choose whichever speaks most to your artistic flair and propose a card based on that one, or both. #1 "Marrowfield Organics" with a slogan something like....." When merely growing green merely isn't quite enough" OR #2 "Quillbrook Organics" with a slogan similar to...."The cutting edge in cleaner, purer organics" OR #3" "Tandrel Organics" with a slogan similar to: "Building a healthier future for those we leave behind"" OR #4 "Loamwise Path" with a slogan similar to: "Purity by Simplicity"
Eventually we will need assistance with web design, promotional and sales materials, etc. so if you offer those services, please indicate that with the design, though it is NOT necessary to offer any additional services to win this contest. WE will pick the winner solely on the business card we like the most.
We want something that stands out, and especially with the name "Oda's organics", we understand that a creative mind may wander into certain attention getting means that may not be quite within the realm of what we can hand out at our local grocer or farmers market. We definitely are not opposed to a little salacious undertone or allusion to attract attention, but please keep it tasteful if you skirt that grey area.
For our card, we use an online printer that can add foils, special die cuts, double sided cards, 3-d cards (we love these 32 pt cards), transparent or translucent cards and more. We love cards that have some of these things where possible and on all of our other business' cards we get rave reviews from customers about their uniqueness. plumtessa.com has the info on these accents if you wish to view what I am referencing.
So in conclusion, we want a unique, stylish, bold, vivid, 2 sided business card that will really stand out. Just usw a generic phone number and website for now and we will add them as they become available. Please email with any questions! Thanks in advance for your effort and creativity!
Target Market(s)
We are targeting parents who are conceintous of what their children and families are eating. Our target audience are moms, but we don't want to exclude anyone else who chooses to eat more healthy. Our target customer is the same customer that would shop at Brightcart stores or local farmers markets

```html
<!DOCTYPE html>
<html lang="en">
<head>
<meta charset="utf-8">
<title>Oda's Organics — Business Card</title>
<link rel="stylesheet" href="https://fonts.googleapis.com/css2?family=Arimo:wght@400;700&display=swap">
<style>
  :root {
    --purple: #4b3f8f;
    --purple-light: #6e62b3;
    --green: #8cc63f;
    --white: #ffffff;
    --ink: #1f1f1f;
    --backdrop: #e8e5e0;
  }
  * { box-sizing: border-box; margin: 0; padding: 0; }
  html, body { width: 1200px; height: 855px; overflow: hidden; }
  body {
    background: var(--backdrop);
    font-family: "Arimo", Arial, sans-serif;
    position: relative;
  }
  .card {
    position: absolute;
    top: 267px;
    width: 560px;
    height: 320px;
    border-radius: 24px;
    background: var(--white);
    overflow: hidden;
    box-shadow: 0 6px 18px rgba(0,0,0,.18);
  }
  .card--front { left: 30px; }
  .card--back { left: 610px; }
  .card svg.card__art { position: absolute; inset: 0; }

  .brand__name { position: absolute; font-weight: 700; font-size: 34px; color: var(--purple); white-space: nowrap; }
  .slogan { position: absolute; font-size: 15px; color: var(--ink); white-space: nowrap; }

  .card--front .brand__name { left: 48px; top: 58px; }
  .card--front .slogan { left: 50px; top: 112px; }
  .website {
    position: absolute; left: 0; right: 0; top: 236px;
    text-align: center; color: var(--white);
    font-weight: 700; font-size: 32px;
    transform: rotate(-4deg);
  }

  .card--back .brand__name { left: 40px; top: 28px; color: var(--white); font-size: 30px; }
  .card--back .slogan { left: 42px; top: 76px; color: var(--white); }

  .contact { position: absolute; left: 56px; top: 168px; list-style: none; }
  .contact__item { display: flex; align-items: center; gap: 16px; height: 46px; font-size: 19px; color: var(--ink); white-space: nowrap; }
  .contact__icon { width: 38px; height: 38px; flex: none; }
</style>
</head>
<body>

<section class="card card--front" aria-label="Card front">
  <svg class="card__art" width="560" height="320" viewBox="0 0 560 320" aria-hidden="true">
    <defs>
      <linearGradient id="bandFront" x1="0" y1="0" x2="1" y2="0">
        <stop offset="0" stop-color="#4b3f8f"/>
        <stop offset=".55" stop-color="#6e62b3"/>
        <stop offset="1" stop-color="#4b3f8f"/>
      </linearGradient>
    </defs>
    <path d="M0 212 L560 172 L560 320 L0 320 Z" fill="url(#bandFront)"/>
    <path d="M0 206 L560 166" stroke="#8cc63f" stroke-width="5"/>
    <path d="M0 312 L560 300" stroke="#8cc63f" stroke-width="5"/>
  </svg>
  <p class="brand__name">Oda's Organics</p>
  <p class="slogan">" Grown clean, the way the garden meant it"</p>
  <p class="website">www.OdasOrganics.com</p>
</section>

<section class="card card--back" aria-label="Card back">
  <svg class="card__art" width="560" height="320" viewBox="0 0 560 320" aria-hidden="true">
    <defs>
      <linearGradient id="bandBack" x1="0" y1="0" x2="1" y2="0">
        <stop offset="0" stop-color="#4b3f8f"/>
        <stop offset=".5" stop-color="#6e62b3"/>
        <stop offset="1" stop-color="#4b3f8f"/>
      </linearGradient>
    </defs>
    <path d="M0 0 H560 V108 Q300 150 0 132 Z" fill="url(#bandBack)"/>
    <path d="M0 132 Q300 150 560 108" fill="none" stroke="#8cc63f" stroke-width="5"/>
  </svg>
  <p class="brand__name">Oda's Organics</p>
  <p class="slogan">" Grown clean, the way the garden meant it"</p>

  <ul class="contact">
    <li class="contact__item">
      <svg class="contact__icon" viewBox="0 0 38 38" aria-hidden="true">
        <circle cx="19" cy="19" r="17" fill="#4b3f8f" stroke="#8cc63f" stroke-width="3"/>
        <path d="M13 11 l4 0 l1.5 5 l-2.5 2 a12 12 0 0 0 6 6 l2 -2.5 l5 1.5 l0 4 a2 2 0 0 1 -2 2 a17 17 0 0 1 -16 -16 a2 2 0 0 1 2 -2 z" fill="#ffffff"/>
      </svg>
      <span>555-014-2837</span>
    </li>
    <li class="contact__item">
      <svg class="contact__icon" viewBox="0 0 38 38" aria-hidden="true">
        <circle cx="19" cy="19" r="17" fill="#4b3f8f" stroke="#8cc63f" stroke-width="3"/>
        <rect x="10" y="13" width="18" height="12" rx="1.5" fill="#ffffff"/>
        <path d="M10 13 L19 20 L28 13" fill="none" stroke="#4b3f8f" stroke-width="1.6"/>
      </svg>
      <span>odasorganics@fernpost.com</span>
    </li>
    <li class="contact__item">
      <svg class="contact__icon" viewBox="0 0 38 38" aria-hidden="true">
        <circle cx="19" cy="19" r="17" fill="#4b3f8f" stroke="#8cc63f" stroke-width="3"/>
        <path d="M19 29 C14 22 12 19 12 16 a7 7 0 0 1 14 0 c0 3 -2 6 -7 13 z" fill="#ffffff"/>
        <circle cx="19" cy="16" r="2.6" fill="#4b3f8f"/>
      </svg>
      <span>48 Orchard Lane, Cedar Hollow, VA 23451</span>
    </li>
  </ul>
</section>

</body>
</html>
```